Varrow Business Card Design - Professional Flexible and forward thinking. Clean and Easy to follow

Management Consulting Company. I focus on business development and concept and operational review. I need a progressive, simple and professional layout design for the business cards, letterhead and envelops
Professional Flexible and forward thinking. Clean and Easy to follow
Mature Business persons and professionals and Corporations

Target Market(s)

Mature Business persons and professionals and Corporations - Government org.

Industry/Entity Type

Consulting

Contact Information for Business Card

Requirements
Must have
• Marcus Varrow
• President
• Phone - 347.682.1530
• email - Mvarrow@varrowpartners-example.com
• Skype - Marc.varrow
• 2187 Tollbrook Lane
• Suite A
• Harlow Point, N.Y. 11492
• USA
Nice to have
• www.varrowpartners-example.com
Should not have
• N/A

```html
<!DOCTYPE html>
<html lang="en">
<head>
<meta charset="utf-8">
<title>Varrow Business Card Design</title>
<link href="https://fonts.googleapis.com/css2?family=Raleway:wght@500&family=Source+Sans+3:wght@400;700&display=swap" rel="stylesheet">
<style>
  :root {
    --backdrop: #e6e7e8;
    --brand-orange: #f5841f;
    --card-white: #ffffff;
    --text-grey: #808285;
    --rule-grey: #c7c8ca;
    --logo-grey: #939598;
  }
  * { margin: 0; padding: 0; box-sizing: border-box; }
  html, body {
    width: 1200px; height: 960px; overflow: hidden;
    background: var(--backdrop);
    font-family: "Source Sans 3", Arial, sans-serif;
  }
  .canvas { position: relative; width: 1200px; height: 960px; }

  .card { position: absolute; left: 270px; width: 646px; height: 368px; }
  .card--front { top: 83px; background: var(--brand-orange); }
  .card--back { top: 507px; background: var(--card-white); }

  .brand-dot { position: absolute; border-radius: 50%; }
  .brand { position: absolute; display: inline-flex; flex-direction: column; align-items: flex-end; }
  .brand__name { font-family: "Raleway", Arial, sans-serif; font-weight: 500; line-height: 1; white-space: nowrap; }
  .brand__site { white-space: nowrap; line-height: 1; }

  .card--front .brand-dot { left: 108px; top: 169px; width: 30px; height: 30px; background: var(--card-white); }
  .card--front .brand { left: 230px; top: 157px; }
  .card--front .brand__name { font-size: 36px; color: var(--card-white); }
  .card--front .brand__site { margin-top: 4px; font-size: 16px; color: var(--card-white); }

  .card--back .brand-dot { left: 40px; top: 80px; width: 18px; height: 18px; background: var(--brand-orange); }
  .card--back .brand { left: 115px; top: 74px; }
  .card--back .brand__name { font-size: 22px; color: var(--logo-grey); }
  .card--back .brand__site { margin-top: 3px; font-size: 11px; color: var(--text-grey); }

  .holder__name {
    position: absolute; left: 40px; top: 199px;
    font-size: 18px; font-weight: 700; line-height: 24px; color: var(--brand-orange);
  }
  .holder__role {
    position: absolute; left: 40px; top: 223px;
    font-size: 14px; line-height: 20px; color: var(--text-grey);
  }
  .holder__rule {
    position: absolute; left: 104px; top: 231px; width: 498px; height: 1px;
    background: var(--rule-grey);
  }

  .contact-list { position: absolute; left: 40px; top: 263px; list-style: none; }
  .contact-list li {
    display: flex; align-items: center; height: 21px;
    font-size: 15px; color: var(--text-grey);
  }
  .contact-list svg { width: 13px; height: 13px; margin-right: 11px; flex: none; }

  .address {
    position: absolute; right: 44px; top: 304px; text-align: right;
    font-size: 15px; line-height: 21px; color: var(--text-grey); font-style: normal;
  }
</style>
</head>
<body>
<div class="canvas">

  <section class="card card--front" aria-label="Card front">
    <span class="brand-dot"></span>
    <div class="brand">
      <span class="brand__name">varrowpartners</span>
      <span class="brand__site">www.varrowpartners-example.com</span>
    </div>
  </section>

  <section class="card card--back" aria-label="Card back">
    <span class="brand-dot"></span>
    <div class="brand">
      <span class="brand__name">varrowpartners</span>
      <span class="brand__site">www.varrowpartners-example.com</span>
    </div>

    <h1 class="holder__name">MARCUS VARROW</h1>
    <p class="holder__role">President</p>
    <span class="holder__rule"></span>

    <ul class="contact-list">
      <li>
        <svg viewBox="0 0 16 16" aria-hidden="true"><path d="M3.5 1.5l2.5 3-1.5 1.8c.8 1.8 2.4 3.4 4.2 4.2l1.8-1.5 3 2.5-1.5 2.5C7.5 14 2 8.5 1 3z" fill="var(--brand-orange)"/></svg>
        347.682.1530
      </li>
      <li>
        <svg viewBox="0 0 16 16" aria-hidden="true"><rect x="1.5" y="3.5" width="13" height="9" fill="none" stroke="var(--brand-orange)" stroke-width="1.3"/><path d="M1.5 3.5L8 9l6.5-5.5" fill="none" stroke="var(--brand-orange)" stroke-width="1.3"/></svg>
        Mvarrow@varrowpartners-example.com
      </li>
      <li>
        <svg viewBox="0 0 16 16" aria-hidden="true"><g fill="none" stroke="var(--brand-orange)" stroke-width="1.2"><circle cx="8" cy="8" r="6.5"/><ellipse cx="8" cy="8" rx="3" ry="6.5"/><path d="M1.5 8h13M2.5 4.8h11M2.5 11.2h11"/></g></svg>
        www.varrowpartners-example.com
      </li>
      <li>
        <svg viewBox="0 0 16 16" aria-hidden="true"><circle cx="8" cy="8" r="7" fill="var(--brand-orange)"/></svg>
        Marc.varrow
      </li>
    </ul>

    <address class="address">
      2187 Tollbrook Lane, Suite A<br>
      Harlow Point, N.Y. 11492, USA
    </address>
  </section>

</div>
</body>
</html>
```